Web design required

1-We need a web design for existing company based in New Zealand
2-We build residential house and light commercial
3-We has in-house designer which allow us can provide interior design
4-We modeling project before site construction, which enable both client and construction team to visually analysis whole project,

Target Market(s)

middle class residential house market
Ref: http://www.brambleworthbuilders.co.nz/

Industry/Entity Type

Construction Company

Number of Pages Required

1 page

Font styles to use
Sans Serif
Other font styles liked:
• Such as : Central Gothic or similar which has more design taste

Colors

Designer to choose colors to be used in the design.

Requirements
Must have
• Front sheet, contact information, sample project

```html
<!DOCTYPE html>
<html lang="en">
<head>
<meta charset="utf-8">
<title>Kestrel Homes</title>
<link href="https://fonts.googleapis.com/css2?family=Roboto:wght@300;400;500;700&display=swap" rel="stylesheet">
<style>
:root{
  --blue:#2179b0;
  --blue-bright:#2a8ad0;
  --ink:#222222;
  --muted:#777777;
  --card-light:#3d3d3d;
  --card-dark:#2e2e2e;
  --footer:#2b2b2b;
  --footer-bar:#222222;
  --white:#ffffff;
  --line:#cfd6db;
}
*{margin:0;padding:0;box-sizing:border-box}
html,body{width:1200px;height:2550px;overflow:hidden}
body{position:relative;font-family:'Roboto',sans-serif;color:var(--ink);background:var(--white)}
.abs{position:absolute}

/* hero */
.hero{left:0;top:0;width:1200px;height:550px;background:linear-gradient(160deg,#3a3d3f 0%,#26292b 45%,#4a4d4f 75%,#333 100%)}
.brand{display:flex;align-items:center;gap:10px;color:var(--white);font-weight:700;font-size:22px;letter-spacing:2px}
.brand-mark{width:26px;height:26px;border-radius:50%;background:var(--blue)}
.top-brand{left:45px;top:24px}
.support-btn{left:997px;top:24px;width:116px;height:32px;border-radius:16px;background:var(--blue);color:var(--white);font-size:13px;display:flex;align-items:center;justify-content:center}
.menu-icon{left:1140px;top:31px}
.hero-title{left:0;width:1200px;top:190px;text-align:center;color:var(--white);font-size:52px;font-weight:500;line-height:1}
.hero-title span{color:var(--blue-bright)}
.hero-sub{left:0;width:1200px;top:257px;text-align:center;color:#e6e6e6;font-size:13px}
.outline-btn{display:flex;align-items:center;justify-content:center;font-size:12px;font-weight:500;letter-spacing:.5px}
.hero-btn{left:537px;top:303px;width:125px;height:35px;border:1px solid var(--blue-bright);color:var(--white)}

/* services */
.service{top:550px;height:270px;color:var(--white);text-align:center}
.service.light{background:var(--card-light)}
.service.dark{background:var(--card-dark)}
.service-num{position:absolute;left:0;right:0;top:30px;font-size:80px;font-weight:700;color:rgba(255,255,255,.04)}
.service h3{position:absolute;left:0;right:0;top:66px;font-size:19px;font-weight:500;letter-spacing:.5px}
.service p{position:absolute;left:62px;right:62px;top:104px;font-size:12px;line-height:26px;color:#d6d6d6}
.service .arrow{position:absolute;left:50%;top:198px;margin-left:-11px}

/* about */
.about-photo{left:172px;top:884px;width:438px;height:246px;background:linear-gradient(135deg,#4f504c 0%,#77736a 40%,#2f2f2d 100%)}
.about-title{left:660px;top:888px;font-size:19px;font-weight:500;letter-spacing:.3px}
.about-text{left:660px;top:925px;width:356px;font-size:12px;line-height:26px;color:var(--muted)}
.about-btn{left:660px;top:1095px;width:127px;height:35px;border:1px solid var(--blue);color:var(--ink)}

/* section heads */
.section-head{left:0;width:1200px;text-align:center}
.section-head h2{font-size:19px;font-weight:500;letter-spacing:.3px}
.section-head p{margin-top:10px;font-size:12px;color:var(--muted)}
.section-head svg{display:block;margin:16px auto 0}

/* gallery */
.tile{top:1330px;width:226px;height:270px}
.tile.grey{background:linear-gradient(160deg,#f1f1f1 0%,#d9d9d9 55%,#bdbdbd 100%)}
.tile.featured{left:483px;top:1325px;width:238px;height:280px;border:5px solid var(--blue);background:linear-gradient(165deg,#5d6e73 0%,#cfd6d8 45%,#1c1c1c 75%,#3a2a22 100%)}
.gallery-nav{left:553px;top:1648px}

/* steps */
.step{width:230px}
.step h4{display:flex;align-items:center;gap:12px;font-size:12px;font-weight:500;letter-spacing:.4px}
.step p{margin-left:33px;margin-top:16px;font-size:12px;line-height:22px;color:var(--muted)}

/* subscribe */
.subscribe{left:0;top:2083px;width:1200px;height:137px;background:var(--blue)}
.subscribe h3{position:absolute;left:247px;top:56px;font-size:19px;font-weight:500;color:var(--white)}
.subscribe .field{position:absolute;left:442px;top:45px;width:513px;height:47px;border:1px solid rgba(255,255,255,.75);border-bottom:none;color:var(--white);font-size:12px;padding:14px 18px}
.subscribe .field::after{content:"";position:absolute;left:0;right:45px;bottom:0;border-bottom:1px solid rgba(255,255,255,.75)}
.subscribe .send{position:absolute;left:918px;top:62px}

/* footer */
.footer{left:0;top:2220px;width:1200px;height:265px;background:var(--footer);color:var(--white)}
.footer .brand{position:absolute;left:172px;top:66px}
.footer-about{position:absolute;left:172px;top:124px;width:220px;font-size:11px;line-height:22px;color:#dcdcdc}
.footer-col{position:absolute;top:64px}
.footer-col h5{font-size:12px;font-weight:500;letter-spacing:.4px}
.footer-col ul{list-style:none;margin-top:20px;font-size:11px;line-height:22px;color:#dcdcdc}
.social{display:flex;gap:14px;margin-top:18px}
.social span{width:15px;height:15px;border-radius:50%;background:var(--white)}
.footer-bar{left:0;top:2485px;width:1200px;height:65px;background:var(--footer-bar);color:var(--white);font-size:11px}
.footer-bar .copy{position:absolute;left:172px;top:26px}
.footer-bar nav{position:absolute;left:710px;top:26px;display:flex;gap:26px;font-weight:500}
</style>
</head>
<body>

<header class="abs hero" role="img" aria-label="Dark modern interior hallway with glass railing and plants"></header>
<div class="abs brand top-brand"><span class="brand-mark"></span>KESTREL HOMES</div>
<div class="abs support-btn">Support</div>
<svg class="abs menu-icon" width="18" height="14" viewBox="0 0 18 14"><g stroke="#fff" stroke-width="1.6"><line x1="0" y1="1" x2="18" y2="1"/><line x1="0" y1="7" x2="18" y2="7"/><line x1="0" y1="13" x2="18" y2="13"/></g></svg>
<h1 class="abs hero-title">WE MAKE <span>YOU</span> HAPPY</h1>
<p class="abs hero-sub">Lorem ipsum dolor sit amet, consectetur adipisicing elit, sed do eiusmod</p>
<a class="abs outline-btn hero-btn">LEARN MORE</a>

<section class="abs service light" style="left:0;width:398px">
  <div class="service-num">01</div>
  <h3>RESIDENTIAL</h3>
  <p>Lorem ipsum dolor sit amet, consectetur adipisicing elit, sed do eiusmod tempor incididunt ut labore et dolore magna aliqua. Ut enim ad</p>
  <svg class="arrow" width="22" height="12" viewBox="0 0 22 12"><path d="M0 6h20M15 1l5 5-5 5" stroke="#2a8ad0" stroke-width="2" fill="none"/></svg>
</section>
<section class="abs service dark" style="left:398px;width:401px">
  <div class="service-num">02</div>
  <h3>COMMERCIAL</h3>
  <p>Lorem ipsum dolor sit amet, consectetur adipisicing elit, sed do eiusmod tempor incididunt ut labore et dolore magna aliqua. Ut enim ad</p>
  <svg class="arrow" width="22" height="12" viewBox="0 0 22 12"><path d="M0 6h20M15 1l5 5-5 5" stroke="#2a8ad0" stroke-width="2" fill="none"/></svg>
</section>
<section class="abs service light" style="left:799px;width:401px">
  <div class="service-num">03</div>
  <h3>INTERIOR DESIGN</h3>
  <p>Lorem ipsum dolor sit amet, consectetur adipisicing elit, sed do eiusmod tempor incididunt ut labore et dolore magna aliqua. Ut enim ad</p>
  <svg class="arrow" width="22" height="12" viewBox="0 0 22 12"><path d="M0 6h20M15 1l5 5-5 5" stroke="#2a8ad0" stroke-width="2" fill="none"/></svg>
</section>

<section class="about">
  <div class="abs about-photo" role="img" aria-label="Bedroom with large window overlooking hills"></div>
  <h2 class="abs about-title">ABOUT KESTREL HOMES</h2>
  <p class="abs about-text">Lorem ipsum dolor sit amet, consectetur adipisicing elit, sed do eiusmod tempor incididunt ut labore et dolore magna aliqua. Ut enim ad minim veniam, quis nostrud exercitation ullamco laboris nisi ut aliquip ex ea commodo consequat. Duis aute irure dolor in reprehenderit in</p>
  <a class="abs outline-btn about-btn">READ MORE</a>
</section>

<div class="abs section-head" style="top:1222px">
  <h2>FEATURED DESIGN</h2>
  <p>Lorem ipsum dolor sit amet, consectetur adipisicing elit, sed do eiusmod</p>
  <svg width="76" height="18" viewBox="0 0 76 18"><line x1="0" y1="9" x2="28" y2="9" stroke="#cfd6db"/><line x1="48" y1="9" x2="76" y2="9" stroke="#cfd6db"/><rect x="32" y="3" width="12" height="12" fill="#2179b0" transform="rotate(45 38 9)"/></svg>
</div>

<div class="abs tile grey" style="left:5px" role="img" aria-label="White kitchen with window"></div>
<div class="abs tile grey" style="left:246px" role="img" aria-label="White kitchen with island"></div>
<div class="abs tile featured" role="img" aria-label="Modern kitchen with black counter and pendant lights"></div>
<div class="abs tile grey" style="left:729px" role="img" aria-label="Bright kitchen with pendant lamps"></div>
<div class="abs tile grey" style="left:970px" role="img" aria-label="Open plan kitchen with island"></div>
<svg class="abs gallery-nav" width="98" height="10" viewBox="0 0 98 10"><g stroke="#888" fill="none"><path d="M2 5h44M6 1L2 5l4 4"/><path d="M52 5h44M92 1l4 4-4 4"/></g></svg>

<div class="abs section-head" style="top:1700px">
  <h2>HOW TO CREATE DESIGN</h2>
  <p>Lorem ipsum dolor sit amet, consectetur adipisicing elit, sed do eiusmod</p>
  <svg width="76" height="18" viewBox="0 0 76 18"><line x1="0" y1="9" x2="28" y2="9" stroke="#cfd6db"/><line x1="48" y1="9" x2="76" y2="9" stroke="#cfd6db"/><rect x="32" y="3" width="12" height="12" fill="#2179b0" transform="rotate(45 38 9)"/></svg>
</div>

<div class="abs step" style="left:172px;top:1818px">
  <h4><svg width="20" height="20" viewBox="0 0 20 20"><path d="M3 17l1-4L14 3l3 3L7 16z M12 5l3 3" stroke="#555" stroke-width="1.4" fill="none"/></svg>DESIGN &amp; DRAWINGS</h4>
  <p>Lorem ipsum dolor sit amet, consectetur adipisicing elit, sed do</p>
</div>
<div class="abs step" style="left:464px;top:1818px">
  <h4><svg width="20" height="20" viewBox="0 0 20 20"><g stroke="#555" stroke-width="1.6" fill="none"><path d="M16 8a6.5 6.5 0 0 0-12-1"/><path d="M4 12a6.5 6.5 0 0 0 12 1"/><path d="M3 3v4h4M17 17v-4h-4"/></g></svg>REBUILD DESIGN</h4>
  <p>Lorem ipsum dolor sit amet, consectetur adipisicing elit, sed do</p>
</div>
<div class="abs step" style="left:780px;top:1818px">
  <h4><svg width="20" height="20" viewBox="0 0 20 20"><g stroke="#555" stroke-width="1.5" fill="none"><circle cx="7" cy="7" r="3.5"/><circle cx="14" cy="14" r="3"/><path d="M7 1.5v2M7 10.5v2M1.5 7h2M10.5 7h2M14 9.5v1.5M14 17v1.5M9.5 14h1.5M17 14h1.5"/></g></svg>CUSTOM DESIGN</h4>
  <p>Lorem ipsum dolor sit amet, consectetur adipisicing elit, sed do</p>
</div>
<div class="abs step" style="left:172px;top:1952px">
  <h4><svg width="20" height="20" viewBox="0 0 20 20"><path d="M3 17l1-4L14 3l3 3L7 16z M12 5l3 3" stroke="#555" stroke-width="1.4" fill="none"/></svg>DESIGN &amp; DRAWINGS</h4>
  <p>Lorem ipsum dolor sit amet, consectetur adipisicing elit, sed do</p>
</div>
<div class="abs step" style="left:464px;top:1952px">
  <h4><svg width="20" height="20" viewBox="0 0 20 20"><g stroke="#555" stroke-width="1.6" fill="none"><path d="M16 8a6.5 6.5 0 0 0-12-1"/><path d="M4 12a6.5 6.5 0 0 0 12 1"/><path d="M3 3v4h4M17 17v-4h-4"/></g></svg>REBUILD DESIGN</h4>
  <p>Lorem ipsum dolor sit amet, consectetur adipisicing elit, sed do</p>
</div>
<div class="abs step" style="left:780px;top:1952px">
  <h4><svg width="20" height="20" viewBox="0 0 20 20"><g stroke="#555" stroke-width="1.5" fill="none"><circle cx="7" cy="7" r="3.5"/><circle cx="14" cy="14" r="3"/><path d="M7 1.5v2M7 10.5v2M1.5 7h2M10.5 7h2M14 9.5v1.5M14 17v1.5M9.5 14h1.5M17 14h1.5"/></g></svg>CUSTOM DESIGN</h4>
  <p>Lorem ipsum dolor sit amet, consectetur adipisicing elit, sed do</p>
</div>

<section class="abs subscribe">
  <h3>SUBSCRIBE US</h3>
  <div class="field">Enter your email...</div>
  <svg class="send" width="24" height="22" viewBox="0 0 24 22"><path d="M1 10L23 1l-6 20-5-7z M12 14l11-13" fill="#fff" stroke="#fff" stroke-width="1" stroke-linejoin="round"/></svg>
</section>

<footer class="abs footer">
  <div class="brand"><span class="brand-mark"></span>KESTREL HOMES</div>
  <p class="footer-about">Lorem ipsum dolor sit amet, consectetur adipisicing elit, sed do eiusmod tempor incididunt ut labore et dolore magna aliqua. Ut enim ad</p>
  <div class="footer-col" style="left:466px">
    <h5>INFOMATION</h5>
    <ul><li>About Us</li><li>Contact Us</li><li>Latest News</li><li>Customs Services</li><li>Support</li></ul>
  </div>
  <div class="footer-col" style="left:684px">
    <h5>LINKS</h5>
    <ul><li>About Us</li><li>Contact Us</li><li>Latest News</li><li>Customs Services</li><li>Support</li></ul>
  </div>
  <div class="footer-col" style="left:904px">
    <h5>FOLLOW US ON</h5>
    <div class="social"><span></span><span></span><span></span><span></span></div>
  </div>
</footer>
<div class="abs footer-bar">
  <p class="copy">Copyright © 2017 Kestrel Homes. All Right Reserved.</p>
  <nav><span>HOME</span><span>CREATE DESIGN</span><span>DESIGN HELP</span><span>CONTACT</span></nav>
</div>

</body>
</html>
```